Business Card Design for Portrait photography professional

We are a small company specializing in portrait photography (weddings, family, couples, children, newborn, pregnant, etc.) Occasionally we do business portraits too and do some other type of photography. We need a business card which would fit into the same look and feel as our website theme (lumvika.com - under construction currently).
Our target customer base lies within mid- to upmarket. We want our business cards to convey a feeling of quality, solidness and a bit luxury.
Design should be universal and usable on 85mmx55mm, 90mmx50mm and 90mmx55mm
one extra file (PSD of a website didn't fit into the allowed updoad, therefore has put it into my filecrate: https://www.filecrate-example.net/s/qt7wk2rbvx9dmhe/website%20theme%20PSD.psd)

Target Market(s)

mostly private people, 25-60 years old, mostly well established.

Industry/Entity Type

Portrait Photography

Requirements
Must have
• 2 sided design (print on both sides of the business card).
Must include:
business name, logo, URL (lumvika.no) , employee name, email address, and phone number.
Colorscheme of the website lumvika.no / lumvika.com

```html
<!DOCTYPE html>
<html lang="en">
<head>
<meta charset="utf-8">
<title>Lumvika – Business Card</title>
<link rel="stylesheet" href="https://fonts.googleapis.com/css2?family=Questrial&family=Josefin+Sans:wght@300;400&display=swap">
<style>
  :root {
    --page-bg: #ececec;
    --card-base: #0b0d0d;
    --card-glow: #262a2a;
    --silver: #d9dcdc;
    --silver-dim: #9ea3a3;
    --divider: rgba(220, 225, 225, 0.22);
    --card-w: 760px;
    --card-h: 465px;
  }
  * { box-sizing: border-box; margin: 0; padding: 0; }
  html, body { width: 1200px; height: 1000px; overflow: hidden; }
  body {
    background: var(--page-bg);
    font-family: "Questrial", sans-serif;
    position: relative;
  }
  .card {
    position: absolute;
    left: 220px;
    width: var(--card-w);
    height: var(--card-h);
    background:
      radial-gradient(ellipse 55% 60% at 55% 40%, var(--card-glow), transparent 75%),
      var(--card-base);
    box-shadow: 0 6px 18px rgba(0,0,0,0.25);
    overflow: hidden;
    color: var(--silver);
  }
  .card--front { top: 25px; }
  .card--back { top: 510px; }

  /* Front */
  .front-panel {
    position: absolute;
    left: 0; top: 0;
    width: 430px; height: 100%;
    background: linear-gradient(180deg, rgba(255,255,255,0.03), rgba(255,255,255,0) 70%);
    border-right: 1px solid var(--divider);
  }
  .tagline {
    position: absolute;
    right: 350px;
    top: 205px;
    text-align: right;
  }
  .tagline__title {
    font-family: "Josefin Sans", sans-serif;
    font-weight: 300;
    font-size: 30px;
    letter-spacing: 1px;
    color: var(--silver);
  }
  .tagline__url {
    font-size: 12px;
    letter-spacing: 1.5px;
    color: var(--silver-dim);
    margin-top: 6px;
  }
  .brand {
    position: absolute;
    left: 470px;
    top: 120px;
    width: 220px;
    height: 220px;
    display: flex;
    align-items: center;
    justify-content: center;
  }
  .brand__ring {
    position: absolute;
    inset: 0;
    border: 2px solid var(--silver);
    border-radius: 50%;
  }
  .brand__name {
    font-family: "Josefin Sans", sans-serif;
    font-weight: 300;
    font-size: 28px;
    letter-spacing: 5px;
    color: var(--silver);
  }

  /* Back */
  .back-divider {
    position: absolute;
    left: 385px;
    top: 110px;
    width: 1px;
    height: 210px;
    background: var(--divider);
  }
  .contact-list {
    position: absolute;
    right: 405px;
    top: 128px;
    list-style: none;
    text-align: right;
    font-size: 15px;
    color: var(--silver-dim);
  }
  .contact-list li { height: 28px; line-height: 28px; }
  .icon-list {
    position: absolute;
    left: 398px;
    top: 128px;
    list-style: none;
  }
  .icon-list li {
    height: 28px;
    display: flex;
    align-items: center;
  }
  .icon-list svg { width: 16px; height: 16px; fill: var(--silver-dim); }
  .employee {
    position: absolute;
    left: 440px;
    top: 193px;
  }
  .employee__name {
    font-size: 18px;
    letter-spacing: 1px;
    color: var(--silver);
  }
  .employee__role {
    font-size: 13px;
    letter-spacing: 1px;
    color: var(--silver-dim);
    margin-top: 3px;
  }
</style>
</head>
<body>

<section class="card card--front" aria-label="Business card front">
  <div class="front-panel"></div>
  <div class="tagline">
    <p class="tagline__title">PERSONAL PHOTOGRAPHER</p>
    <p class="tagline__url">WWW.LUMVIKA.COM</p>
  </div>
  <div class="brand">
    <span class="brand__ring"></span>
    <span class="brand__name">LUMVIKA</span>
  </div>
</section>

<section class="card card--back" aria-label="Business card back">
  <ul class="contact-list">
    <li>555 555 5555</li>
    <li>Your Address</li>
    <li>Yourmail@webpage.com</li>
    <li>Chirpnet.com/YourName</li>
  </ul>
  <div class="back-divider"></div>
  <ul class="icon-list" aria-hidden="true">
    <li><svg viewBox="0 0 16 16"><path d="M2 5c0-1.5 2.5-2.5 6-2.5s6 1 6 2.5v1.5h-3V5H5v1.5H2z"/><rect x="3.5" y="7.5" width="9" height="6" rx="1"/></svg></li>
    <li><svg viewBox="0 0 16 16"><path d="M8 1a4.5 4.5 0 0 0-4.5 4.5C3.5 9 8 15 8 15s4.5-6 4.5-9.5A4.5 4.5 0 0 0 8 1zm0 6.3a1.8 1.8 0 1 1 0-3.6 1.8 1.8 0 0 1 0 3.6z"/></svg></li>
    <li><svg viewBox="0 0 16 16"><path d="M1.5 3.5h13v9h-13z M1.5 3.5 8 9l6.5-5.5" fill="none" stroke="#9ea3a3" stroke-width="1.4"/></svg></li>
    <li><svg viewBox="0 0 16 16"><circle cx="8" cy="8" r="6"/></svg></li>
  </ul>
  <div class="employee">
    <p class="employee__name">EMPLOYEE NAME</p>
    <p class="employee__role">EMPLOYEE ROLE</p>
  </div>
</section>

</body>
</html>
```